Business Card Design Project

Corwen Property Management

Our Business is residential property management, we therefore need a card that displays a professional image, but is clear and concise, and easy to read
Updates

We are committed now guys and girls, loving what we are seeing so far! 

Target Market(s)

Landlords, Rental Property Owners

Industry/Entity Type

Residential

Requirements
Must have
• Dean Fosterly - Principal
Tessa Fosterly - Director (Property Management)

PO Box 718
Holloway SA 5093

Dean: 0419 372 508
Tessa: 0419 613 947

www.corwenpropertymanagement.com.au
admin@corwenpropertymanagement.com.au

Nice to have
• I would like the card to be double sided, white background on the information side and then colour on the reverse, in blue or black and incorporating our logo

```html
<!DOCTYPE html>
<html lang="en">
<head>
<meta charset="utf-8">
<title>Corwen Property Management – Business Card</title>
<link rel="stylesheet" href="https://fonts.googleapis.com/css2?family=Open+Sans:ital,wght@0,400;0,600;0,700;1,700&display=swap">
<style>
  :root {
    --backdrop: #e7e4df;
    --card-white: #ffffff;
    --ink-dark: #4a4a4c;
    --ink-grey: #7b7b7d;
    --ink-text: #333335;
    --brand-blue: #1f5fa6;
    --accent-blue: #1f88c9;
    --light-blue: #4aa7dd;
    --back-blue: #4a93c8;
    --back-grey: #5b5f62;
    --bullet: #555557;
  }
  * { margin: 0; padding: 0; box-sizing: border-box; }
  html, body { width: 1200px; height: 750px; overflow: hidden; }
  body {
    background: var(--backdrop);
    font-family: "Open Sans", Arial, sans-serif;
    position: relative;
  }
  .card {
    position: absolute;
    top: 217px;
    width: 503px;
    height: 331px;
    overflow: hidden;
    box-shadow: 0 4px 14px rgba(0,0,0,0.18);
  }
  .card--front { left: 62px; background: var(--card-white); }
  .card--back {
    left: 625px;
    background: linear-gradient(125deg, var(--back-blue) 0%, var(--back-blue) 45%, var(--back-grey) 100%);
  }

  .wordmark { position: absolute; display: flex; align-items: center; }
  .wordmark__square { flex: none; }
  .wordmark__text { font-weight: 700; line-height: 1; }
  .wordmark__name { display: block; letter-spacing: -1px; }
  .wordmark__sub { display: block; letter-spacing: 0.3px; }

  .card--front .wordmark { left: 30px; top: 20px; }
  .card--front .wordmark__square { width: 54px; height: 54px; background: var(--accent-blue); margin-right: 14px; }
  .card--front .wordmark__text { color: var(--ink-dark); }
  .card--front .wordmark__name { font-size: 50px; }
  .card--front .wordmark__sub { font-size: 12.5px; margin-top: 3px; margin-left: 2px; }

  .card--back .wordmark { left: 58px; top: 112px; }
  .card--back .wordmark__square { width: 56px; height: 56px; background: #ffffff; margin-right: 22px; }
  .card--back .wordmark__text { color: #ffffff; }
  .card--back .wordmark__name { font-size: 80px; }
  .card--back .wordmark__sub { font-size: 19px; margin-top: 4px; margin-left: 4px; }

  .contact { position: absolute; left: 16px; top: 106px; }
  .contact__row { position: relative; white-space: nowrap; line-height: 21px; }
  .contact__row--bullet::before {
    content: ""; position: absolute; left: 0; top: 8px;
    width: 7px; height: 7px; background: var(--bullet);
  }
  .contact__row { padding-left: 12px; }
  .contact__row--indent { padding-left: 10px; }
  .person { font-style: italic; font-weight: 700; font-size: 19px; color: var(--brand-blue); }
  .role { font-size: 16px; font-weight: 600; color: var(--ink-grey); }
  .role--small { font-size: 9px; font-weight: 600; }
  .address { font-size: 16.5px; font-weight: 600; color: var(--accent-blue); }
  .phone-label { font-size: 16.5px; font-weight: 600; color: var(--accent-blue); }
  .phone-number { font-size: 16.5px; font-weight: 600; color: var(--ink-grey); letter-spacing: 0.5px; }
  .gap { height: 2px; }

  .online { position: absolute; left: 16px; top: 262px; }
  .online__line { font-size: 14.5px; font-weight: 600; color: var(--ink-text); line-height: 20px; }

  .corner-block {
    position: absolute; right: 0; bottom: 0;
    width: 112px; height: 112px;
    background: linear-gradient(160deg, var(--light-blue), var(--accent-blue));
  }
</style>
</head>
<body>
  <section class="card card--front" aria-label="Card front">
    <div class="wordmark">
      <span class="wordmark__square"></span>
      <span class="wordmark__text">
        <span class="wordmark__name">Corwen</span>
        <span class="wordmark__sub">Property Management</span>
      </span>
    </div>

    <div class="contact">
      <p class="contact__row contact__row--bullet"><span class="person">Dean Fosterly</span> <span class="role">Principal</span></p>
      <p class="contact__row contact__row--indent"><span class="person">Tessa Fosterly</span> <span class="role">Director</span> <span class="role role--small">(Property Management)</span></p>
      <div class="gap"></div>
      <p class="contact__row contact__row--bullet"><span class="address">PO Box 718</span></p>
      <p class="contact__row"><span class="address">Holloway SA 5093</span></p>
      <p class="contact__row contact__row--bullet"><span class="phone-label">Dean:</span> <span class="phone-number">0419 372 508</span></p>
      <div class="gap"></div>
      <p class="contact__row"><span class="phone-label">Tessa:</span> <span class="phone-number">0419 613 947</span></p>
    </div>

    <div class="online">
      <p class="online__line">www.corwenpropertymanagement.com.au</p>
      <p class="online__line">admin@corwenpropertymanagement.com.au</p>
    </div>

    <div class="corner-block"></div>
  </section>

  <section class="card card--back" aria-label="Card back">
    <div class="wordmark">
      <span class="wordmark__square"></span>
      <span class="wordmark__text">
        <span class="wordmark__name">Corwen</span>
        <span class="wordmark__sub">Property Management</span>
      </span>
    </div>
  </section>
</body>
</html>
```